Emerging Australian photographer

I'm based in Cunderdin, a small rural town in the Wheatbelt area of Western Australia. So its a good thing that I love to travel further afield both for pleasure and for work. To me that is one and the same thing in any event!

My desire is to take photos that make the viewers heart skip. I love taking photos of people doing the things they love or being with the people they love. For me, the joy of photography comes with capturing the 'moments between the moments'. I like candid photography best of all - like when the new husband is staring joyfully at his bride and at that minute is unaware of the photographer capturing the moment.

I am available for weddings, engagements, birthdays, special events, newborns, family or individual portraits. By the end of the year I will be accredited with the Coastal Guild of Image Makers.

I need a card that stands out but is elegant and would sit well on the table at a wedding or be given out in the church grounds. Classy and a little bit sassy.

Target Market(s)

Consumers who are seeking photographic services, eg wedding guests who see me at work and make enquiries.

Industry/Entity Type

Church

Contact Information for Business Card

Delia Marchetti Photography
Delia Marchetti
0452 368 071
www.deliamarchetti.com.au
photos@deliamarchetti.com.au

Requirements
Must have
• Must fit with the theme in the watermarks, but be crisp and modern.
Nice to have
• However it's not essential to have the pink! Chatterbook and Peeper logos.
Should not have
• Old style fonts like times new roman.

```html
<!DOCTYPE html>
<html lang="en">
<head>
<meta charset="utf-8">
<title>Delia Marchetti Photography – Business Card</title>
<link rel="stylesheet" href="https://fonts.googleapis.com/css2?family=Italianno&family=Raleway:wght@300&display=swap">
<style>
  :root {
    --page-bg: #ffffff;
    --front-bg: #fdf6f8;
    --front-pattern-tone: #fbe9ee;
    --back-bg: #3d3d3d;
    --back-pattern-tone: #5a5a5a;
    --ink-grey: #5f5f5f;
    --accent-pink: #f0b3cc;
    --contact-ink: #dcdcdc;
    --card-shadow: 0 4px 10px rgba(0,0,0,0.18);
  }
  * { margin: 0; padding: 0; box-sizing: border-box; }
  html, body {
    width: 1200px; height: 1200px; overflow: hidden;
    background: var(--page-bg);
  }
  .canvas { position: relative; width: 1200px; height: 1200px; }
  .card {
    position: absolute; left: 254px; width: 694px; height: 422px;
    box-shadow: var(--card-shadow); overflow: hidden;
  }
  .card--front { top: 145px; }
  .card--back { top: 632px; }
  .card-pattern { position: absolute; inset: 0; }
  .card--front .card-pattern {
    background: radial-gradient(circle at 50% 45%, var(--front-bg) 0%, var(--front-pattern-tone) 100%);
  }
  .card--back .card-pattern {
    background: linear-gradient(135deg, var(--back-pattern-tone) 0%, var(--back-bg) 55%, var(--back-pattern-tone) 100%);
  }
  .brand {
    position: absolute; left: 0; right: 0; top: 110px;
    display: flex; flex-direction: column; align-items: center;
  }
  .brand-dot {
    width: 18px; height: 18px; border-radius: 50%;
    background: var(--accent-pink); margin-bottom: 34px;
  }
  .brand-name {
    font-family: "Raleway", sans-serif; font-weight: 300;
    font-size: 40px; letter-spacing: 1px; color: var(--ink-grey);
  }
  .holder-name {
    position: absolute; left: 118px; top: 112px;
    font-family: "Italianno", cursive; font-size: 80px; line-height: 1;
    color: var(--accent-pink); font-weight: 400;
  }
  .contact-list {
    position: absolute; left: 126px; top: 230px; list-style: none;
  }
  .contact-item {
    display: flex; align-items: center; height: 40px;
    font-family: "Raleway", sans-serif; font-weight: 300;
    font-size: 21px; letter-spacing: 1.5px; color: var(--contact-ink);
  }
  .contact-icon { width: 20px; height: 20px; margin-right: 9px; flex: none; }
</style>
</head>
<body>
<main class="canvas">
  <section class="card card--front" aria-label="Card front">
    <div class="card-pattern" role="img" aria-label="Faint pale pink diamond pattern background"></div>
    <div class="brand">
      <span class="brand-dot"></span>
      <span class="brand-name">delia marchetti photography</span>
    </div>
  </section>

  <section class="card card--back" aria-label="Card back">
    <div class="card-pattern" role="img" aria-label="Grey diamond pattern on charcoal background"></div>
    <h1 class="holder-name">Delia Marchetti</h1>
    <ul class="contact-list">
      <li class="contact-item">
        <svg class="contact-icon" viewBox="0 0 20 20" aria-hidden="true">
          <circle cx="10" cy="10" r="10" fill="#f0b3cc"/>
          <rect x="7" y="4.5" width="6" height="11" rx="1.2" fill="none" stroke="#3d3d3d" stroke-width="1.3"/>
          <circle cx="10" cy="13.3" r="0.8" fill="#3d3d3d"/>
        </svg>
        <span>0452 368 071</span>
      </li>
      <li class="contact-item">
        <svg class="contact-icon" viewBox="0 0 20 20" aria-hidden="true">
          <circle cx="10" cy="10" r="10" fill="#f0b3cc"/>
          <rect x="5" y="6.5" width="10" height="7" fill="none" stroke="#3d3d3d" stroke-width="1.2"/>
          <path d="M5 6.5 L10 10.8 L15 6.5" fill="none" stroke="#3d3d3d" stroke-width="1.2"/>
        </svg>
        <span>photos@deliamarchetti.com.au</span>
      </li>
      <li class="contact-item">
        <svg class="contact-icon" viewBox="0 0 20 20" aria-hidden="true">
          <circle cx="10" cy="10" r="10" fill="#f0b3cc"/>
          <circle cx="10" cy="10" r="5.2" fill="none" stroke="#3d3d3d" stroke-width="1.1"/>
          <ellipse cx="10" cy="10" rx="2.2" ry="5.2" fill="none" stroke="#3d3d3d" stroke-width="1"/>
          <line x1="4.8" y1="10" x2="15.2" y2="10" stroke="#3d3d3d" stroke-width="1"/>
        </svg>
        <span>www.deliamarchetti.com.au</span>
      </li>
    </ul>
  </section>
</main>
</body>
</html>
```